Business Card Design Project

We require business cards for "Venoth". We are composed of elite prior military personnel. Our goal is to provide site security for premium businesses who want on the most professional of agents on their premises. Additionally, we will provide executive protection for individuals who require professionalism, flexibility, and dedication

We want this business card to communicate professionalism, dependability, strength. However, we are not an overtly tactical agency and do not want to intimidate our clients personnel or their client. We want to give them a sense of security.
Updates

At the request of one of the designers I've listed the appropriate text that should appear on the card. Please feel free to arrange it in a creative and professional manor.

I've also uploaded a .png file of the triangle logo with no text. Please feel free to incorporate this into your designs.

ThanksĀ 

Target Market(s)

Premium businesses, executives, celebrities, and governments.

Industry/Entity Type

Security

Requirements
Must have
• Text Info that will go on the card. It does not have to be in this order:
Name
Title
Office Phone Number
Cell Phone Number
Email
Website
Mailing Address
Nice to have
• On the back I'd like to see the triangle portion of the logo displayed in a creative way that leaves enough room to write down information if needed.
Should not have
• - Weapons, Globes, or Shields. Every rent-a-cop company has that, and that's not what we are.

```html
<!DOCTYPE html>
<html lang="en">
<head>
<meta charset="utf-8">
<title>Venoth Business Card</title>
<link href="https://fonts.googleapis.com/css2?family=Cinzel:wght@400;600&display=swap" rel="stylesheet">
<style>
  :root {
    --page-bg: #e6e9ed;
    --card-deep: #081d33;
    --card-mid: #0f3457;
    --card-light: #174a75;
    --band-dark: #071628;
    --band-edge: #8d97a6;
    --orb-light: #7cc6ee;
    --orb-mid: #2d8ccc;
    --orb-deep: #0d3d66;
    --ring-light: #c4ccd8;
    --ring-dark: #5d6677;
    --text-white: #f2f5f8;
    --text-blue: #3aa0e4;
    --text-soft: #6fb4e6;
    --brand-faint: #2f6ea6;
  }
  * { margin: 0; padding: 0; box-sizing: border-box; }
  html, body {
    width: 1200px;
    height: 1000px;
    overflow: hidden;
    background: var(--page-bg);
    font-family: "Cinzel", serif;
  }
  .sheet {
    position: relative;
    width: 1200px;
    height: 1000px;
  }
  .card {
    position: absolute;
    left: 220px;
    width: 760px;
    height: 447px;
    overflow: hidden;
    background:
      radial-gradient(ellipse at 60% 55%, var(--card-light) 0%, var(--card-mid) 45%, var(--card-deep) 100%);
    box-shadow: 0 6px 18px rgba(0, 0, 0, 0.25);
  }
  .card--front { top: 33px; }
  .card--back { top: 520px; }

  /* front */
  .brand-band {
    position: absolute;
    left: 150px;
    top: 88px;
    width: 640px;
    height: 144px;
    background: linear-gradient(180deg, #0b2038 0%, var(--band-dark) 100%);
    border: 4px solid var(--band-edge);
    border-right: none;
    border-radius: 14px 0 0 14px;
  }
  .brand-name {
    position: absolute;
    left: 306px;
    top: 88px;
    height: 144px;
    display: flex;
    align-items: center;
    gap: 18px;
    font-weight: 600;
    font-size: 52px;
    line-height: 1;
    letter-spacing: 2px;
    color: var(--text-white);
  }
  .brand-dot {
    flex: none;
    width: 34px;
    height: 34px;
    border-radius: 50%;
    background: var(--text-blue);
  }
  .orb {
    position: absolute;
    left: 40px;
    top: 44px;
    width: 236px;
    height: 236px;
  }
  .contact {
    position: absolute;
    right: 32px;
    top: 252px;
    text-align: right;
  }
  .contact__name {
    font-size: 20px;
    font-weight: 600;
    color: var(--text-white);
    font-variant: small-caps;
  }
  .contact__title {
    font-size: 21px;
    color: var(--text-blue);
    margin-top: 2px;
  }
  .contact__list {
    list-style: none;
    margin-top: 14px;
    font-size: 13.5px;
    line-height: 17px;
    color: var(--text-soft);
  }

  /* back */
  .back-mark {
    position: absolute;
    left: 0;
    right: 0;
    top: 150px;
    display: flex;
    flex-direction: column;
    align-items: center;
    gap: 26px;
  }
  .back-mark__square {
    width: 120px;
    height: 120px;
    background: var(--brand-faint);
    opacity: 0.45;
  }
  .back-mark__name {
    font-weight: 600;
    font-size: 34px;
    letter-spacing: 2px;
    color: var(--brand-faint);
  }
</style>
</head>
<body>
<main class="sheet">
  <section class="card card--front">
    <div class="brand-band"></div>
    <svg class="orb" viewBox="0 0 236 236" role="img" aria-label="Glossy blue lens emblem in a silver ring">
      <defs>
        <linearGradient id="ring" x1="0" y1="0" x2="1" y2="1">
          <stop offset="0" stop-color="var(--ring-light)"/>
          <stop offset="1" stop-color="var(--ring-dark)"/>
        </linearGradient>
        <radialGradient id="lens" cx="0.4" cy="0.35" r="0.7">
          <stop offset="0" stop-color="var(--orb-light)"/>
          <stop offset="0.55" stop-color="var(--orb-mid)"/>
          <stop offset="1" stop-color="var(--orb-deep)"/>
        </radialGradient>
      </defs>
      <circle cx="118" cy="118" r="114" fill="url(#ring)"/>
      <circle cx="118" cy="118" r="100" fill="var(--band-dark)"/>
      <circle cx="124" cy="122" r="86" fill="url(#lens)"/>
    </svg>
    <div class="brand-name"><span class="brand-dot"></span><span>VENOTH</span></div>
    <div class="contact">
      <p class="contact__name">Name Goes Here, Jr</p>
      <p class="contact__title">TITLE GOES HERE</p>
      <ul class="contact__list">
        <li>Office Phone Number</li>
        <li>Cell Phone Number</li>
        <li>Email</li>
        <li>Website</li>
        <li>Mailing Address</li>
      </ul>
    </div>
  </section>

  <section class="card card--back">
    <div class="back-mark">
      <span class="back-mark__square"></span>
      <span class="back-mark__name">VENOTH</span>
    </div>
  </section>
</main>
</body>
</html>
```